Sleek wordpress site for Brightwell finishing systems

We are a commercial job shop that serves B2B, govt & LEO and retail clients.We need a wordpress site with 6 individual pages: homepage, coating, laser engraving, laser cutting, part marking, and contact us. I have attached an outline of the desired flow and sub headings for each page. I would like to incorporate the colors of the logo through out the site to be clean and sleek enough to appeal to B2B commercial clients yet be inviting enough for retail clients.

I would like to have easy picture functionality so photographs on each page can be updated easily.

Target Market(s)

B2B industrial & Govt and Military part marking, laser engraving and coating: machine shops, aerospace companies, tool manufactures. Retail: personalized gifts, Job Shop

Coding

Coded - Design and coding required

Font styles to use
Sans Serif
Other font styles liked:
• Open to suggestion

Colors
0255a3
3176b5
eaf1f7
cfdeed
ffffff

Requirements
Must have
• Clean easy to navigate flow, separate pages as indicated on attached outline, high class feel. Great picture functionality, professional and inviting feel,
• **update: needs to be optimized for mobile, should have a gallery function. Gallery can be an additional page or embedded
Nice to have
• Social media connectivity links,
Should not have
• crappy plugins that make back-end management difficult, no blog

```html
<!DOCTYPE html>
<html lang="en">
<head>
<meta charset="utf-8">
<title>Brightwell finishing systems</title>
<link href="https://fonts.googleapis.com/css2?family=Montserrat:wght@400;600;700&family=Open+Sans:wght@400;600&display=swap" rel="stylesheet">
<style>
:root{
  --blue:#0255a3;
  --blue-mid:#3176b5;
  --ice:#eaf1f7;
  --mist:#cfdeed;
  --white:#ffffff;
  --ink:#555b63;
  --muted:#8a9099;
  --footer:#5e6064;
  --field:#eef3f8;
}
*{margin:0;padding:0;box-sizing:border-box}
html,body{width:721px;height:1200px;overflow:hidden;background:var(--white)}
body{position:relative;font-family:"Open Sans",sans-serif;color:var(--ink)}
.abs{position:absolute}
.brand{display:flex;align-items:center;gap:5px;font-family:"Montserrat",sans-serif;font-weight:700;color:var(--blue);font-size:8px;text-transform:uppercase;line-height:1.15}
.brand-dot{width:22px;height:22px;border-radius:50%;background:var(--blue);flex:none}
.header-call{left:356px;top:19px;font-family:"Montserrat",sans-serif;font-size:9px;color:var(--blue);display:flex;align-items:center;gap:3px}
.header-call b{color:var(--ink);font-weight:400}
.socials{display:flex;gap:4px}
.socials span{width:12px;height:12px;border-radius:50%;background:#5b5e63;display:block}
.socials span.on{background:var(--blue)}
.login{left:535px;top:15px;width:92px;height:20px;border:1px solid var(--blue-mid);color:var(--blue);font-family:"Montserrat",sans-serif;font-size:6px;font-weight:600;letter-spacing:.5px;display:flex;align-items:center;justify-content:center}
.nav{left:243px;top:47px;display:flex;gap:15px;font-family:"Montserrat",sans-serif;font-size:6.4px;color:#555;letter-spacing:.3px}
.nav a{color:inherit;text-decoration:none;position:relative;padding-bottom:9px}
.nav a.active{color:var(--blue)}
.nav a.active::after{content:"";position:absolute;left:-5px;right:-5px;bottom:0;height:2px;background:var(--blue)}
.hero-side{top:72px;height:216px;background:linear-gradient(135deg,#c9ccd0,#aeb3b8);opacity:.7}
.hero{left:94px;top:72px;width:533px;height:216px;background:linear-gradient(135deg,#6f6a5e,#3d3d3b 55%,#2a2b2c);color:var(--white);text-align:center}
.hero h1{font-family:"Montserrat",sans-serif;font-weight:700;font-size:22px;margin-top:68px;letter-spacing:.3px}
.hero p{font-size:7.6px;width:350px;margin:6px auto 0;line-height:1.4}
.hero .btn-white{display:inline-block;margin-top:14px;width:77px;height:20px;line-height:20px;background:var(--white);color:var(--blue);font-family:"Montserrat",sans-serif;font-size:6px;font-weight:600;letter-spacing:.5px}
.dots{position:absolute;left:0;right:0;bottom:18px;display:flex;justify-content:center;gap:4px}
.dots i{width:5px;height:5px;border-radius:50%;border:1px solid var(--white)}
.dots i.on{background:var(--blue);border-color:var(--blue)}
.pager{top:149px;width:20px;height:62px;border:1px solid var(--blue-mid);color:var(--blue);font-family:"Montserrat",sans-serif;font-size:6px;display:flex;flex-direction:column;align-items:center;justify-content:center;gap:4px}
.pager.next{background:var(--blue);color:var(--white)}
.section-title{left:0;width:721px;text-align:center;font-family:"Open Sans",sans-serif;font-size:16px;color:var(--blue-mid)}
.card{top:358px;width:123px;height:120px;color:var(--white);font-family:"Montserrat",sans-serif;font-weight:600;font-size:8px;display:flex;flex-direction:column;align-items:center;justify-content:center;text-align:center;text-transform:uppercase}
.card.c1{background:linear-gradient(135deg,#4a4a48,#222)}
.card.c2{background:linear-gradient(135deg,#6b6660,#3a3937)}
.card.c3{background:linear-gradient(135deg,#5c6570,#2f3440)}
.card.c4{background:linear-gradient(135deg,#8793a6,#4e5a6e)}
.card .blurb{text-transform:none;font-family:"Open Sans",sans-serif;font-weight:400;font-size:6.4px;line-height:1.35;margin-top:6px;width:100px}
.card .mini{margin-top:6px;border:1px solid var(--white);font-size:5px;letter-spacing:.5px;padding:3px 14px}
.btn{height:20px;font-family:"Montserrat",sans-serif;font-size:6px;font-weight:600;letter-spacing:.5px;display:flex;align-items:center;justify-content:center;border:1px solid var(--blue-mid);color:var(--blue)}
.btn.solid{background:var(--blue-mid);color:var(--white)}
.about{left:0;top:556px;width:721px;height:225px;background:var(--ice);text-align:center}
.about .mark{width:26px;height:26px;border-radius:50%;background:var(--blue);margin:40px auto 0}
.about h2{font-weight:400;font-size:16px;color:var(--blue-mid);margin-top:6px}
.about p{font-size:7px;line-height:1.5;width:425px;margin:14px auto 0;color:#666}
.about .btn{width:91px;margin:16px auto 0}
.field{background:var(--field);font-size:6.5px;color:#a3a9b0;padding:6px 9px}
.footer{left:0;top:1022px;width:721px;height:178px;background:var(--footer);color:#eee}
.footer .brand{color:var(--white)}
.footer .brand-dot{background:var(--white)}
.footer h4{font-family:"Montserrat",sans-serif;font-size:7.6px;font-weight:600;color:var(--white)}
.footer .small{font-size:6.6px;line-height:1.6}
.quick a{display:block;color:#eee;text-decoration:none;font-size:7px;line-height:11.5px}
.quick a.on{color:var(--blue-mid)}
.to-top{left:597px;top:1054px;width:19px;height:19px;border-radius:50%;background:var(--blue-mid);display:flex;align-items:center;justify-content:center}
.rule{left:79px;top:1160px;width:563px;height:1px;background:#8b8d91}
.footer-social span{background:#d8d9db}
.footer-social span.on{background:var(--blue-mid)}
</style>
</head>
<body>

<header>
  <div class="abs brand" style="left:95px;top:18px"><span class="brand-dot"></span><span>Brightwell<br>finishing systems</span></div>
  <div class="abs header-call">Call Us
    <svg width="10" height="10" viewBox="0 0 24 24"><path fill="none" stroke="#0255a3" stroke-width="2.2" d="M6 3l3 4-2 2c1 3 4 6 7 7l2-2 4 3-2 3C10 20 4 14 3 5z"/></svg>
    <b>555.214.0380</b></div>
  <div class="abs socials" style="left:465px;top:20px"><span></span><span class="on"></span><span></span><span></span></div>
  <div class="abs login">
    <svg width="6" height="6" viewBox="0 0 10 10" style="margin-right:4px"><circle cx="5" cy="3" r="2.3" fill="#0255a3"/><path d="M1 10c0-3 2-4.5 4-4.5S9 7 9 10z" fill="#0255a3"/></svg>LOGIN / REGISTER</div>
  <nav class="abs nav">
    <a class="active">HOME</a><a>ABOUT US</a><a>LASER ENGRAVING</a><a>LASER CUTTING</a><a>PART MARKING</a><a>COATINGS</a><a>CONTACT US</a>
  </nav>
</header>

<div class="abs hero-side" style="left:0;width:94px" role="img" aria-label="Previous slide photograph of firearm parts"></div>
<div class="abs hero-side" style="left:627px;width:94px" role="img" aria-label="Next slide photograph of firearm parts"></div>
<section class="abs hero" role="img" aria-label="Photograph of laser engraved rifles and handgun parts">
  <h1>LASER ENGRAVING</h1>
  <p>Capabilities Statement: With our selection of CO2 and fiber lasers there are very few materials and substrates that we cannot mark or engrave...</p>
  <span class="btn-white">READ MORE</span>
  <div class="dots"><i></i><i class="on"></i><i></i><i></i></div>
</section>
<div class="abs pager" style="left:30px"><span>P</span><span>R</span><span>E</span><span>V</span></div>
<div class="abs pager next" style="left:671px"><span>N</span><span>E</span><span>X</span><span>T</span></div>

<h2 class="abs section-title" style="top:321px;font-weight:400">Our Services</h2>
<div class="abs card c1" style="left:93px" role="img" aria-label="Photograph of engraved handgun and ammunition">Laser Engraving</div>
<div class="abs card c2" style="left:230px" role="img" aria-label="Photograph of laser cutting work">Laser Cutting
  <span class="blurb">Laser cutting is a non-contact cutting process with a kurf width of ...</span>
  <span class="mini">READ MORE</span></div>
<div class="abs card c3" style="left:367px" role="img" aria-label="Photograph of hands marking a handgun part">Part Marking</div>
<div class="abs card c4" style="left:504px" role="img" aria-label="Photograph of a coated rifle being handled">Coatings</div>
<div class="abs btn" style="left:250px;top:498px;width:106px">CALL US: 555.214.0380</div>
<div class="abs btn solid" style="left:365px;top:498px;width:106px">GET A FREE QUOTE</div>

<section class="abs about">
  <div class="mark"></div>
  <h2>About Us</h2>
  <p>There are many variations of passages of Lorem Ipsum available, but the majority have suffered alteration in some form, by injected humour, or randomised words which don't look even slightly believable. If you are going to use a passage of Lorem Ipsum, you need to be sure there isn't anything embarrassing hidden in the middle of text. All the Lorem Ipsum generators on the Internet tend to repeat predefined chunks ...</p>
  <div class="btn">DISCOVER MORE</div>
</section>

<h2 class="abs section-title" style="top:813px;font-weight:400">Send Us Message</h2>
<div class="abs field" style="left:139px;top:850px;width:147px;height:18px">Type you Name</div>
<div class="abs field" style="left:297px;top:850px;width:147px;height:18px">Enter your Email</div>
<div class="abs field" style="left:456px;top:850px;width:125px;height:18px">Phone</div>
<div class="abs field" style="left:139px;top:880px;width:442px;height:72px;padding-top:8px">Type your Message</div>
<div class="abs btn solid" style="left:332px;top:964px;width:57px">SEND</div>

<footer class="abs footer">
  <div class="abs brand" style="left:94px;top:42px"><span class="brand-dot"></span><span>Brightwell<br>finishing systems</span></div>
  <div class="abs small" style="left:94px;top:96px">© 2018 brightwell finishing systems.<br>All Right Reserved.</div>
  <h4 class="abs" style="left:284px;top:36px">Contact Us</h4>
  <div class="abs" style="left:284px;top:54px;font-size:13px;color:var(--white)">Call Us: 555.214.0380</div>
  <div class="abs small" style="left:284px;top:74px">info@brightwellfinishing.com</div>
  <div class="abs small" style="left:284px;top:96px">418 N Cedar Row #12, Tempe,<br>AZ 85281</div>
  <h4 class="abs" style="left:490px;top:36px">Quick Link</h4>
  <div class="abs quick" style="left:490px;top:50px">
    <a>About Us</a><a class="on">Laser engraving</a><a>Laser Cutting</a><a>Part Marking</a><a>Coatings</a><a>Contact Us</a>
  </div>
</footer>
<div class="abs to-top"><svg width="8" height="8" viewBox="0 0 10 10"><path d="M5 9V1M2 4l3-3 3 3" stroke="#fff" stroke-width="1.4" fill="none"/></svg></div>
<div class="abs rule"></div>
<div class="abs socials footer-social" style="left:332px;top:1174px"><span></span><span class="on"></span><span></span><span></span></div>

</body>
</html>
```